Hallo liebe Designer,
wir haben bereits ein Design, welches sich an den Farben unserer Homepage www.lorta.de orientiert. Dieses Design muss nachgebaut werden. Wir benötigen eine editierbare Microsoft-WORD-Datei, die nach Bedarf angepasst werden kann (falls sich Telefonnummer oder ähnliches mal ändert)
Zusammengefasst:
Benötigt wird: Ein Worddokument mit einem Briefpapier mit der Hauptseite und Folgeseiten. Die Folgeseiten sollen automatisch entstehen, wenn mehr wie 1 Seite beschrieben wird.
Das Design bitte so nachbauen wie es im PDF ersichtlich ist.
- das Worddokument muss anpassbar sein, falls sich mal die Telefonnummer o.ä. ändert

```html
<!DOCTYPE html>
<html lang="de">
<head>
<meta charset="utf-8">
<title>LOR Unternehmensgruppe – Briefpapier</title>
<link href="https://fonts.googleapis.com/css2?family=Carlito:wght@400&family=Questrial&display=swap" rel="stylesheet">
<style>
  :root {
    --paper: #fdfdfd;
    --canvas: #ffffff;
    --frame: #3a3a3a;
    --ink: #2b2b2b;
    --footer-ink: #6f6f6f;
    --brand-dark: #7a7f78;
    --brand-light: #a0a89f;
  }
  * { box-sizing: border-box; margin: 0; padding: 0; }
  html, body { width: 1200px; height: 835px; overflow: hidden; background: var(--canvas); }
  .sheet-canvas { position: relative; width: 1200px; height: 835px; }
  .page {
    position: absolute; top: 125px; width: 416px; height: 587px;
    background: var(--paper); border: 1px solid var(--frame); overflow: hidden;
  }
  .page--first { left: 161px; }
  .page--follow { left: 625px; }

  .brand {
    position: absolute; left: 388px; top: 176px; left: auto; right: 42px; top: 52px;
    display: flex; align-items: center; gap: 6px;
    font-family: "Questrial", sans-serif; color: var(--brand-dark);
  }
  .brand__dot { width: 14px; height: 14px; border-radius: 50%; background: var(--brand-dark); }
  .brand__name { font-size: 15px; letter-spacing: 0.2px; }

  .sender-line {
    position: absolute; left: 39px; top: 102px;
    font-family: "Carlito", sans-serif; font-size: 4.7px; color: var(--ink);
  }

  .letter-body {
    position: absolute; left: 42px; top: 138px; width: 331px;
    font-family: "Carlito", sans-serif; font-size: 7.35px; line-height: 18px;
    color: var(--ink); text-align: justify;
  }
  .letter-body p.opening { text-indent: 39px; }

  .footer-info {
    position: absolute; left: 39px; top: 530px; display: flex;
    font-family: "Questrial", sans-serif; font-size: 5.4px; line-height: 6.6px;
    color: var(--footer-ink);
  }
  .footer-info__col { padding-right: 8px; }
  .footer-info__col + .footer-info__col { border-left: 0.8px solid var(--footer-ink); padding-left: 7px; }
  .footer-info__col--management { width: 82px; }
  .footer-info__col--bank { width: 115px; }
  .contact-row { display: flex; align-items: center; gap: 3px; }
  .contact-row svg { width: 4px; height: 4px; fill: var(--footer-ink); }

  .footer-band { position: absolute; left: 0; bottom: 0; width: 100%; height: 26px; }
  .footer-band svg { position: absolute; inset: 0; width: 100%; height: 100%; }
  .footer-band__url {
    position: absolute; right: 26px; bottom: 8px;
    font-family: "Questrial", sans-serif; font-size: 11.5px; color: #ffffff; letter-spacing: 0.3px;
  }
</style>
</head>
<body>
<div class="sheet-canvas">

  <section class="page page--first">
    <div class="brand">
      <span class="brand__dot"></span>
      <span class="brand__name">LOR Unternehmensgruppe</span>
    </div>
    <div class="sender-line">LOR Unternehmensgruppe GmbH, Lindenhofer Weg 27, 63101 Bergstedt</div>

    <div class="letter-body">
      <p class="opening">Lorem ipsum dolor sit amet, consectetur adipiscing elit. Nullam congue ac ex nec tincidunt. Aliquam metus velit, dignissim at porttitor a, sagittis at sem. Vivamus sodales gravida erat at aliquam. In in ultricies nibh. Etiam id urna nec sem ultrices viverra. Nulla facilisi. Duis egestas, lacus eget imperdiet suscipit, elit purus pulvinar ipsum, quis scelerisque purus enim ac dolor. Etiam a nunc sed arcu blandit accumsan. Etiam ut mi quis orci tempor tempor id eu lectus. Donec faucibus libero quam, vitae sagittis nisi pulvinar et. Donec non pharetra dolor. Quisque vel dapibus diam. Nunc hendrerit condimentum hendrerit. Nullam elementum libero eget tortor interdum luctus. Nullam vitae turpis maximus erat mollis tempor in non nisi.</p>
      <p>Maecenas maximus ligula sed velit volutpat viverra. Etiam nec ante sagittis sapien gravida rutrum sed feugiat massa. Donec tempor blandit quam a rhoncus. Pellentesque porttitor est mi, et consectetur sapien pretium non. Mauris hendrerit ante tortor, et luctus quam volutpat et. Sed convallis eu magna eget finibus. Proin facilisis libero ipsum, eu efficitur eros tincidunt quis. Praesent laoreet ex quis enim hendrerit imperdiet.</p>
      <p>Praesent ipsum lorem, volutpat sed dui sed, commodo elementum lectus. Maecenas efficitur pellentesque nulla et fermentum. Etiam tempor, libero id fringilla viverra, felis tellus convallis tellus, non varius sapien sem ut erat. Curabitur luctus nunc at leo sollicitudin, non vestibulum diamLorem ipsum dolor sit amet, consectetur adipiscing elit. Nullam congue ac ex nec tincidunt. Aliquam metus velit, dignissim at porttitor a, sagittis at sem. Vivamus sodales gravida erat at aliquam. In in ultricies nibh. Etiam id urna nec sem ultrices viverra. Nulla facilisi. Duis</p>
    </div>

    <div class="footer-info">
      <div class="footer-info__col footer-info__col--management">Geschäftsführer:<br>Markus Reinhold<br>Sabine Wendler<br>Amtsgericht Bergstedt<br>HRB 48190</div>
      <div class="footer-info__col footer-info__col--bank">Umsatzsteuer-ID<br>DE417260385<br>Stadtbank Nordtal<br>BIC: STNODEXXXXX<br>IBAN : DE12 4700 0000 1234 5678 90</div>
      <div class="footer-info__col footer-info__col--address">Postanschrift :<br>Am Erlengrund 8<br>42110 Talheim
        <div class="contact-row"><svg viewBox="0 0 10 10"><path d="M2 0.5l2 2-1 1.5c0.6 1.3 1.7 2.4 3 3l1.5-1 2 2-1.3 1.5C4 9 1 6 0.5 1.8z"/></svg>+49 210 / 55501230</div>
        <div class="contact-row"><svg viewBox="0 0 10 10"><path d="M0 2h10v6H0z M0 2l5 3.5L10 2"/></svg>info@lorta.de</div>
      </div>
    </div>

    <div class="footer-band">
      <svg viewBox="0 0 416 26" preserveAspectRatio="none">
        <rect x="0" y="16" width="416" height="10" fill="var(--brand-light)"/>
        <polygon points="300,0 416,0 416,26 287,26" fill="var(--brand-dark)"/>
      </svg>
      <span class="footer-band__url">www.lorta.de</span>
    </div>
  </section>

  <section class="page page--follow">
    <div class="letter-body">
      <p>egestas, lacus eget imperdiet suscipit, elit purus pulvinar ipsum, quis scelerisque purus enim ac dolor. Etiam a nunc sed arcu blandit accumsan. Etiam ut mi quis orci tempor tempor id eu lectus. Donec faucibus libero quam, vitae sagittis nisi pulvinar et. Donec non pharetra dolor. Quisque vel dapibus diam. Nunc hendrerit condimentum hendrerit. Nullam elementum libero eget tortor interdum luctus. Nullam vitae turpis maximus erat mollis tempor in non nisi.</p>
    </div>

    <div class="footer-info">
      <div class="footer-info__col footer-info__col--management">Geschäftsführer:<br>Markus Reinhold<br>Sabine Wendler<br>Amtsgericht Bergstedt<br>HRB 48190</div>
      <div class="footer-info__col footer-info__col--bank">Umsatzsteuer-ID<br>DE417260385<br>Stadtbank Nordtal<br>BIC: STNODEXXXXX<br>IBAN : DE12 4700 0000 1234 5678 90</div>
      <div class="footer-info__col footer-info__col--address">Postanschrift :<br>Am Erlengrund 8<br>42110 Talheim
        <div class="contact-row"><svg viewBox="0 0 10 10"><path d="M2 0.5l2 2-1 1.5c0.6 1.3 1.7 2.4 3 3l1.5-1 2 2-1.3 1.5C4 9 1 6 0.5 1.8z"/></svg>+49 210 / 55501230</div>
        <div class="contact-row"><svg viewBox="0 0 10 10"><path d="M0 2h10v6H0z M0 2l5 3.5L10 2"/></svg>info@lorta.de</div>
      </div>
    </div>

    <div class="footer-band">
      <svg viewBox="0 0 416 26" preserveAspectRatio="none">
        <rect x="0" y="16" width="416" height="10" fill="var(--brand-light)"/>
        <polygon points="300,0 416,0 416,26 287,26" fill="var(--brand-dark)"/>
      </svg>
      <span class="footer-band__url">www.lorta.de</span>
    </div>
  </section>

</div>
</body>
</html>
```